Coffee bag stamp design for new coffee brand

Stamp design that will be used like a label on a coffee package.
It must be a vector that can be produced as a stamp. Coffee bag is from brown craft paper. I upload image of this bag. Size of design is 80mm x 140mm.
I also uploaded two pictures for inspiration, but I will also appreciate new ideas.

Target Market(s)

Coffee lovers, who love to try new coffee. Also hipsters.

Colors

Designer to choose only greyscale colors for use in the design.

Requirements
Must have
• Some information about coffee must have:
Name: BRAZIL (the biggest font in that design)
Region: Santos
Altitude: 60 – 1200 m.n.m.
Variety: Arabica
Processing: unwashed

```html
<!DOCTYPE html>
<html lang="en">
<head>
<meta charset="utf-8">
<title>Kestrel Coffee – Brazil Label</title>
<link rel="stylesheet" href="https://fonts.googleapis.com/css2?family=Montserrat:wght@600;700&display=swap">
<style>
  :root {
    --ink: #111111;
    --paper: #ffffff;
  }
  html, body {
    margin: 0;
    padding: 0;
    width: 1200px;
    height: 893px;
    overflow: hidden;
    background: var(--paper);
  }
  .label {
    display: block;
    width: 1200px;
    height: 893px;
  }
  .label__frame-outer { fill: none; stroke: var(--ink); stroke-width: 7; }
  .label__frame-inner { fill: none; stroke: var(--ink); stroke-width: 2.5; }
  .label__rule { stroke: var(--ink); stroke-width: 3; }
  .label__brand-mask { fill: var(--paper); }
  .label__brand-dot { fill: var(--ink); }
  .label__text {
    font-family: "Montserrat", sans-serif;
    fill: var(--ink);
    text-anchor: middle;
  }
  .label__brand { font-weight: 700; }
  .label__origin { font-size: 46px; font-weight: 700; letter-spacing: 1px; }
  .label__detail { font-size: 28px; font-weight: 600; letter-spacing: 0.5px; }
  .label__process-bar { fill: var(--ink); }
  .label__process { font-size: 28px; font-weight: 700; fill: var(--paper); letter-spacing: 0.5px; }
</style>
</head>
<body>
<svg class="label" viewBox="0 0 1200 893" xmlns="http://www.w3.org/2000/svg" aria-label="Kestrel Coffee Brazil label">
  <g transform="scale(1.1719) translate(-208 8)">
    <rect class="label__frame-outer" x="560" y="150" width="323" height="512" rx="14"/>
    <rect class="label__frame-inner" x="572" y="162" width="298" height="488" rx="8"/>

    <rect class="label__brand-mask" x="612" y="130" width="216" height="145"/>
    <circle class="label__brand-dot" cx="720" cy="158" r="20"/>
    <text class="label__text label__brand" x="720" y="222" font-size="40">KESTREL</text>
    <text class="label__text label__brand" x="720" y="256" font-size="22">COFFEE</text>

    <line class="label__rule" x1="596" y1="300" x2="846" y2="300"/>
    <text class="label__text label__origin" x="720" y="352">BRAZIL</text>
    <line class="label__rule" x1="596" y1="366" x2="846" y2="366"/>
    <line class="label__rule" x1="596" y1="372" x2="846" y2="372"/>

    <text class="label__text label__detail" x="720" y="408">SANTOS</text>
    <line class="label__rule" x1="596" y1="428" x2="846" y2="428"/>

    <text class="label__text label__detail" x="720" y="463">60-12- M.N.M.</text>
    <line class="label__rule" x1="596" y1="486" x2="846" y2="486"/>
    <line class="label__rule" x1="596" y1="492" x2="846" y2="492"/>

    <text class="label__text label__detail" x="720" y="522">ARABICA</text>
    <line class="label__rule" x1="596" y1="534" x2="846" y2="534"/>

    <rect class="label__process-bar" x="585" y="565" width="272" height="52"/>
    <text class="label__text label__process" x="721" y="601">UNWASHED</text>
  </g>
</svg>
</body>
</html>
```